Professional looking Roller Blind Discount Card that portrays quality at a value for money price!

We need a double sided business card designed as a discount card. Size 90mm wide x 55mm high.We would like it to look professional and portray quality at a value for money price point.I have uploaded a word document with a basic layout with the information we want included on each side of the card. Please put your own thought into the layout.

Contact Information for Business Card

As per word document attached.

```html
<!DOCTYPE html>
<html lang="en">
<head>
<meta charset="utf-8">
<title>Roller Blinds Discount Card</title>
<link href="https://fonts.googleapis.com/css2?family=Nunito:wght@400;600;800&family=Montserrat:wght@400;500&display=swap" rel="stylesheet">
<style>
  :root {
    --bg: #b9b7b2;
    --card: #ffffff;
    --blue: #36a5df;
    --blue-dark: #1e7fb4;
    --ink: #2b2b2b;
    --photo-a: #5f6b55;
    --photo-b: #8fa27a;
    --photo-c: #b7a58c;
  }
  * { box-sizing: border-box; margin: 0; padding: 0; }
  html, body { width: 1200px; height: 924px; overflow: hidden; }
  body {
    background: var(--bg);
    font-family: "Nunito", sans-serif;
    color: var(--ink);
    display: flex;
    flex-direction: column;
    align-items: center;
    justify-content: center;
    gap: 40px;
  }
  .card {
    width: 640px;
    height: 391px;
    background: var(--card);
    border-bottom: 6px solid var(--blue-dark);
    position: relative;
    overflow: hidden;
  }

  /* Front */
  .front { text-align: center; padding-top: 26px; }
  .front-title {
    font-weight: 800;
    font-size: 44px;
    color: var(--blue);
    line-height: 1.05;
  }
  .front-sub {
    font-family: "Montserrat", sans-serif;
    font-size: 25px;
    letter-spacing: 3px;
    margin-top: 6px;
  }
  .front-photo {
    width: 560px;
    height: 150px;
    margin: 16px auto 0;
    background: linear-gradient(100deg, var(--photo-c) 0%, var(--photo-a) 30%, var(--photo-b) 60%, var(--photo-a) 100%);
  }
  .call {
    font-size: 24px;
    margin-top: 26px;
  }
  .call .phone { color: var(--blue); font-weight: 600; }

  /* Back */
  .back { text-align: center; padding-top: 36px; }
  .offer {
    font-weight: 600;
    font-size: 46px;
    color: var(--blue);
    line-height: 1;
  }
  .offer-sub {
    font-size: 18px;
    margin-top: 22px;
  }
  .features {
    position: absolute;
    left: 0; right: 0;
    top: 200px;
    height: 70px;
    background: var(--blue);
    display: flex;
  }
  .feature {
    flex: 1;
    position: relative;
    border-right: 3px solid var(--card);
    color: var(--card);
    font-size: 14px;
    display: flex;
    align-items: flex-end;
    justify-content: center;
    padding-bottom: 10px;
  }
  .feature:last-child { border-right: none; }
  .feature-icon {
    position: absolute;
    top: -38px;
    left: 50%;
    transform: translateX(-50%);
    width: 64px; height: 64px;
  }
  .back .call { position: absolute; left: 0; right: 0; top: 310px; margin: 0; }
</style>
</head>
<body>
  <section class="card front">
    <h1 class="front-title">Roller Blinds</h1>
    <p class="front-sub">FREE in Home Measure &amp; Quote</p>
    <div class="front-photo" role="img" aria-label="Photo of a room window fitted with roller blinds overlooking a garden"></div>
    <p class="call">Call <span class="phone">0400 123 456</span> Today!</p>
  </section>

  <section class="card back">
    <h2 class="offer">25% OFF</h2>
    <p class="offer-sub">Quality Custom Made Roller Blinds Blockout – Screen – Light Filtering</p>
    <div class="features">
      <div class="feature">
        <svg class="feature-icon" viewBox="0 0 64 64" aria-hidden="true">
          <circle cx="32" cy="32" r="30" fill="#fff" stroke="#36a5df" stroke-width="2"/>
          <path d="M18 32 L32 19 L46 32 M22 29 V45 H42 V29" fill="none" stroke="#36a5df" stroke-width="2" stroke-linejoin="round"/>
          <rect x="29" y="35" width="6" height="10" fill="none" stroke="#36a5df" stroke-width="2"/>
        </svg>
        FREE in Home Measure &amp; Quote
      </div>
      <div class="feature">
        <svg class="feature-icon" viewBox="0 0 64 64" role="img" aria-label="Family icon">
          <circle cx="32" cy="32" r="30" fill="#fff" stroke="#36a5df" stroke-width="2"/>
          <circle cx="32" cy="32" r="18" fill="#d5ecf8"/>
        </svg>
        Family Owned &amp; Operated
      </div>
      <div class="feature">
        <svg class="feature-icon" viewBox="0 0 64 64" aria-hidden="true">
          <circle cx="32" cy="32" r="30" fill="#fff" stroke="#36a5df" stroke-width="2"/>
          <circle cx="32" cy="32" r="14" fill="none" stroke="#36a5df" stroke-width="2"/>
          <text x="32" y="38" text-anchor="middle" font-family="Nunito, sans-serif" font-size="16" font-weight="800" fill="#36a5df">$</text>
        </svg>
        Best Price Guarantee
      </div>
    </div>
    <p class="call">Call <span class="phone">0400 123 456</span> Today!</p>
  </section>
</body>
</html>
```